Cleaning service website design

We need a new nice web design(logo will be the same) for a new cleaning service Company:

Informations about Company and logo you can take from flyers in attachments.

This is a cleaning service Company which have simple rules and we would like to show that(in checklist form) on website:

- What we do and that we're Cleaning Green

- Why us?

- How much(our pricing is simple)

Also we would like to communicate with clients by some nice/big pictures on website and the most important thing is our phone number and short/fast Freestimate.

Also there should be some space for description about our Company.

Generally all information on main page can be short: about us, about service(what we do), last reviews, tips (for example: Tip of the week) and other can be some introduction to subpage where will be more information.

There will be few subpages like: About us, About our service, Photos(Before and after), Reviews , Tips, FAQ, Contact, Looking for a Job? - most of them will be just text so you can project just one example.

```html
<!DOCTYPE html>
<html lang="en">
<head>
<meta charset="utf-8">
<title>Tidy Nest – House Cleaning</title>
<link rel="stylesheet" href="https://fonts.googleapis.com/css2?family=Ubuntu:ital,wght@0,400;0,500;0,700;1,400;1,500;1,700&family=Noto+Serif&display=swap">
<style>
:root{
  --blue:#0b6cc4;
  --head-blue:#1766b4;
  --green:#5aa845;
  --btn-green:#66b04e;
  --light-green:#8fd27a;
  --yellow:#f1f01a;
  --text:#444;
  --muted:#666;
  --panel:#f4f4f4;
  --line:#d2d2d2;
  --footer:#e4e4e4;
}
*{margin:0;padding:0;box-sizing:border-box}
html,body{width:993px;height:1200px;overflow:hidden;background:#fff}
body{font-family:"Ubuntu",sans-serif;color:var(--text)}
.page{position:relative;width:1200px;height:1450px;transform:scale(.8275);transform-origin:0 0;
  background:linear-gradient(#fff 0,#ededed 148px,#fff 148px)}
.abs{position:absolute}
/* header */
.brand{left:130px;top:22px;display:flex;align-items:center;gap:12px}
.brand-dot{width:80px;height:80px;border-radius:50%;background:var(--green)}
.brand-name{font-size:34px;font-weight:500;color:var(--green)}
.call{left:810px;top:34px}
.call svg{position:absolute;left:0;top:14px}
.call-label{margin-left:42px;font-size:19px;font-weight:500;color:var(--blue)}
.call-number{margin-left:42px;font-size:33px;font-weight:500;color:var(--green);line-height:1.2}
.nav{left:130px;top:125px;width:940px;height:44px;background:var(--blue);border-radius:3px;display:flex;align-items:center;overflow:hidden}
.nav a{color:#fff;text-decoration:none;font-size:13px;font-weight:500;height:44px;line-height:44px}
.nav a.active{background:var(--btn-green);padding:0 19px;margin-right:4px}
.nav a+a{margin-left:19px}
/* hero */
.hero{left:130px;top:175px;width:940px;height:386px;border-radius:3px;overflow:hidden;
  background:linear-gradient(90deg,#5caa48 0,#6cbb56 40%,#86cf6f 70%,#6cb75a 100%)}
.hero-photo{position:absolute;left:390px;top:0;width:550px;height:386px;
  background:radial-gradient(ellipse at 50% 55%,#3a3f4a 0,#4a5c70 35%,rgba(120,200,110,0) 70%)}
.hero-title{left:30px;top:38px;font-size:42px;font-weight:700;font-style:italic;color:#fff;line-height:47px}
.hero-bucket{left:25px;top:143px;width:84px;height:96px;border-radius:10px;background:linear-gradient(#c9d0d8,#2c3d6a)}
.hero-service{left:123px;top:142px;font-size:27px;font-style:italic;color:var(--yellow)}
.hero-low{left:124px;top:185px;font-size:17px;font-style:italic;color:#fff}
.hero-currency{left:198px;top:185px;font-size:44px;color:#fff}
.hero-price{left:226px;top:165px;font-size:86px;font-style:italic;color:var(--yellow);line-height:1.1}
.quote-btn{left:31px;top:285px;width:191px;height:37px;border-radius:3px;background:linear-gradient(#fff,#e4e4e4);
  font-size:19px;font-weight:500;color:#333;text-align:center;line-height:37px}
.dots{left:22px;top:355px;display:flex;gap:7px}
.dots span{width:13px;height:13px;border-radius:50%;background:#e8e8e8}
.dots span:first-child{background:var(--blue)}
/* columns */
.col-title{font-size:23px;color:var(--head-blue)}
.col-title .green{color:var(--green)}
.col-title em{font-style:italic}
.photo{border:1px solid #ccc}
.body-text{font-size:13px;line-height:20px;color:var(--text)}
.btn{background:var(--btn-green);color:#fff;font-size:13px;font-weight:500;border-radius:3px;text-align:center;line-height:29px;height:29px}
.checklist{list-style:none}
.checklist li{position:relative;padding-left:27px;font-size:13px;height:26px;line-height:20px}
.checklist li::before{content:"";position:absolute;left:1px;top:6px;width:8px;height:8px;border-radius:50%;background:var(--green)}
.pricing{left:770px;top:628px;width:300px;height:333px;background:var(--panel);border:1px solid var(--line)}
.price-card{position:absolute;left:11px;width:277px;height:65px;background:#fff;border:1px solid var(--line);display:flex;align-items:center}
.price-amount{font-family:"Noto Serif",serif;color:var(--green);width:101px;padding-left:11px;white-space:nowrap}
.price-amount small{font-size:30px}
.price-amount b{font-weight:400;font-size:44px}
.price-label{font-size:14px;font-weight:500;color:var(--blue);line-height:21px}
.price-note{left:11px;top:250px;font-size:13px;line-height:19px;color:var(--text)}
.price-link{left:10px;top:297px;font-size:13px;color:var(--blue)}
/* bottom boxes */
.box{top:994px;width:300px;height:319px;background:var(--panel);border:1px solid #cfcfcf}
.box .col-title{position:absolute;left:15px;top:12px}
.thumb{position:absolute;width:65px;height:57px;border:1px solid #bbb}
.item-title{position:absolute;font-size:15px;font-weight:500;color:var(--green)}
.item-text{position:absolute;font-size:13px;line-height:18px;color:#333}
.posted{position:absolute;font-size:11px;font-style:italic;color:var(--blue)}
.divider{position:absolute;height:1px;background:#ddd}
.quote-text{position:absolute;left:14px;width:262px;font-size:12.4px;font-style:italic;line-height:20px;color:var(--muted)}
.quote-by{position:absolute;right:18px;font-size:15px;font-weight:500;color:var(--green)}
/* footer */
.footer{left:0;top:1328px;width:1200px;height:122px;background:var(--footer)}
.footer-links{left:130px;top:20px;font-size:13px;color:#555}
.footer-links span{margin:0 6px;color:#777}
.copyright{left:130px;top:62px;font-size:13px;line-height:19px;color:#555}
.copyright a{color:var(--blue);text-decoration:none}
.social{left:890px;top:45px;display:flex;gap:8px}
.social span{width:30px;height:30px;border-radius:3px}
</style>
</head>
<body>
<div class="page">

  <header>
    <div class="abs brand">
      <span class="brand-dot"></span>
      <span class="brand-name">Tidy Nest</span>
    </div>
    <div class="abs call">
      <svg width="34" height="38" viewBox="0 0 34 38" aria-hidden="true">
        <path d="M6 2c3-2 6 0 7 3l2 5c1 2 0 4-2 5l-2 1c1 4 5 9 9 11l2-1c2-1 4-1 5 1l3 4c1 2 0 5-3 6-10 2-23-13-24-25 0-4 1-8 3-10z" fill="#c6201c"/>
      </svg>
      <div class="call-label">Call Us Today:</div>
      <div class="call-number">555-014-2290</div>
    </div>
    <nav class="abs nav">
      <a class="active">Home</a>
      <a>About Us</a>
      <a style="margin-left:46px">Our Service</a>
      <a style="margin-left:47px">Photos Gallery</a>
      <a style="margin-left:42px">Reviews</a>
      <a style="margin-left:41px">Tips</a>
      <a style="margin-left:44px">FAQ</a>
      <a style="margin-left:46px">Contact Us</a>
      <a style="margin-left:43px">Looking for a Job?</a>
    </nav>
  </header>

  <section class="abs hero">
    <div class="hero-photo" role="img" aria-label="Smiling cleaning team giving thumbs up with mops, sprays and gloves"></div>
    <h1 class="abs hero-title">Affordably Simpler<br>Making your Life</h1>
    <div class="abs hero-bucket" role="img" aria-label="Bucket of cleaning supplies with a mop"></div>
    <div class="abs hero-service">House Cleaning</div>
    <div class="abs hero-low">as low as</div>
    <div class="abs hero-currency">$</div>
    <div class="abs hero-price">79</div>
    <div class="abs quote-btn">Get A Free Quote</div>
    <div class="abs dots"><span></span><span></span><span></span><span></span></div>
  </section>

  <section>
    <h2 class="abs col-title" style="left:130px;top:585px">About Our Company</h2>
    <div class="abs photo" style="left:130px;top:628px;width:285px;height:150px;background:linear-gradient(#7fa9dd,#9cc2ea 55%,#3d4a3e)" role="img" aria-label="Company owners outdoors on a sunny day"></div>
    <p class="abs body-text" style="left:130px;top:791px;width:290px">We are Daniel and Clara Novak and we have personally experienced the struggle of finding a reliable and affordable maid service. We understand how busy life can be and cleaning is one of the tasks that falls off the list when you’re stretched too thin. We are here to help!</p>
    <div class="abs btn" style="left:341px;top:932px;width:70px">MORE</div>

    <h2 class="abs col-title" style="left:450px;top:585px">What We Do</h2>
    <div class="abs photo" style="left:450px;top:628px;width:285px;height:150px;background:linear-gradient(#e9e6e2,#c89d6e 60%,#a8744a)" role="img" aria-label="Vacuum cleaner on a wooden floor"></div>
    <ul class="abs checklist" style="left:450px;top:791px">
      <li>Making mirrors shine</li>
      <li>Mop or vacuum your floors</li>
      <li>Dust surfaces</li>
      <li>Collect garbage</li>
      <li>Make beds</li>
    </ul>
    <div class="abs btn" style="left:671px;top:931px;width:70px">MORE</div>

    <h2 class="abs col-title" style="left:770px;top:585px"><span class="green">Pricing is..</span> <em>Simple.</em></h2>
    <div class="abs pricing">
      <div class="price-card" style="top:10px"><div class="price-amount"><small>$</small> <b>79</b></div><div class="price-label">For Homes Less than<br>1000 sq ft</div></div>
      <div class="price-card" style="top:88px"><div class="price-amount"><small>$</small> <b>89</b></div><div class="price-label">For Homes<br>1000-1800 sq ft</div></div>
      <div class="price-card" style="top:166px"><div class="price-amount"><small>$</small> <b>99</b></div><div class="price-label">For Homes<br>1800-2600 sq ft</div></div>
      <p class="abs price-note">*If your home is larger than 2600 sq ft<br>please call for a quote.</p>
      <a class="abs price-link">Rates are for Regular Service</a>
    </div>
  </section>

  <section>
    <div class="abs box" style="left:130px">
      <h2 class="col-title">Last Reviews</h2>
      <div class="thumb" style="left:17px;top:52px;background:linear-gradient(#c7a98a,#3b2c22)" role="img" aria-label="Reviewer portrait"></div>
      <div class="item-title" style="left:96px;top:48px">Elena Hart</div>
      <div class="item-text" style="left:96px;top:68px;width:195px">Nunc dignissim lectus vitae eros placerat euismod. Aenean lacinia sodales eros....</div>
      <div class="posted" style="left:96px;top:128px">Posted on 3 days ago</div>
      <div class="divider" style="left:17px;top:154px;width:265px"></div>
      <div class="thumb" style="left:17px;top:168px;background:linear-gradient(#c9d9e9,#d9b79a)" role="img" aria-label="Reviewer portrait"></div>
      <div class="item-title" style="left:96px;top:164px">Elena Hart</div>
      <div class="item-text" style="left:96px;top:184px;width:195px">Nunc dignissim lectus vitae eros placerat euismod. Aenean lacinia sodales eros....</div>
      <div class="posted" style="left:96px;top:244px">Posted on 3 days ago</div>
      <div class="abs btn" style="left:14px;top:279px;width:70px">READ ALL</div>
    </div>

    <div class="abs box" style="left:450px">
      <h2 class="col-title">Tips of the day</h2>
      <div class="thumb" style="left:15px;top:52px;background:linear-gradient(#e7e3de,#b98a5c)" role="img" aria-label="Vacuuming a floor"></div>
      <div class="item-title" style="left:93px;top:48px">Morbi iaculis fringilla..</div>
      <div class="item-text" style="left:93px;top:68px;width:190px">Aenean a nibh eget turpis vehicula tempus ac sed massa.</div>
      <div class="divider" style="left:15px;top:126px;width:265px"></div>
      <div class="thumb" style="left:15px;top:143px;background:linear-gradient(90deg,#f1f1f1,#e6e27a)" role="img" aria-label="Cleaner with spray bottle and yellow gloves"></div>
      <div class="item-title" style="left:93px;top:139px">Morbi iaculis fringilla..</div>
      <div class="item-text" style="left:93px;top:159px;width:190px">Aenean a nibh eget turpis vehicula tempus ac sed massa.</div>
      <div class="divider" style="left:15px;top:217px;width:265px"></div>
      <div class="thumb" style="left:15px;top:233px;background:linear-gradient(90deg,#1d2b58,#e8df2a)" role="img" aria-label="Gloved hands cleaning a surface"></div>
      <div class="item-title" style="left:93px;top:229px">Morbi iaculis fringilla..</div>
      <div class="item-text" style="left:93px;top:249px;width:190px">Aenean a nibh eget turpis vehicula tempus ac sed massa.</div>
    </div>

    <div class="abs box" style="left:770px">
      <h2 class="col-title" style="left:12px;top:10px">Client Says...</h2>
      <p class="quote-text" style="top:42px">Vestibulum vel metus sit amet turpis bibendum tincidunt vel sit amet quam. Pellentesque habi-tant morbi tristique senectus et netus et male-suada fames ac turpis egestas....</p>
      <div class="quote-by" style="top:129px">By Mark Doyle</div>
      <div class="divider" style="left:14px;top:155px;width:270px"></div>
      <p class="quote-text" style="top:166px">Vestibulum vel metus sit amet turpis bibendum tincidunt vel sit amet quam. Pellentesque habi-tant morbi tristique senectus et netus et male-suada fames ac turpis egestas....</p>
      <div class="quote-by" style="top:253px">By Mark Doyle</div>
      <div class="abs btn" style="left:14px;top:277px;width:70px">READ ALL</div>
    </div>
  </section>

  <footer class="abs footer">
    <div class="abs footer-links">Home<span>|</span>About Us<span>|</span>Our Service<span>|</span>Photos Gallery<span>|</span>Reviews<span>|</span>Tips<span>|</span>FAQ<span>|</span>Contact<span>|</span>Looking for a Job?</div>
    <div class="abs copyright">Copyright © 2013. <a>TidyNestHome.</a><br>All Right Reserved</div>
    <div class="abs social" aria-label="Social links">
      <span style="background:#3b5b9a"></span>
      <span style="background:#5cc6e8"></span>
      <span style="background:#1673a8"></span>
      <span style="background:#f07a1c"></span>
      <span style="background:#c9201d"></span>
    </div>
  </footer>

</div>
</body>
</html>
```